Project Halcyon PowerPoint Design

This is a PPT design for Power & Utilities company who are in the process of a technology upgrade for their Finance department. We are looking to develop a branded PPT for Project Halcyon (specifically HALCYON). Why does Halcyon resonate? "The Earth is pointed almost directly at Halcyon. During the course of the night,
Halcyon does not rise or set, but remains in nearly the same spot above the
northern horizon year- round while the other stars circle around it."
Halcyon represents the guiding principles that manage, monitor and
control the organizations financials.

Target Market(s)

Finance stakeholders impacted by technology enhancement

Font styles to use
Serif
Other font styles liked:
• Arial

Colors
0054AA
0677BA
7BADD7
CADEEF
E8F1F8

Requirements
Must have
• Various slide layout ( Cover slide, content slide, divider, etc). Attached is the logo and corporate colors
Nice to have
• Over the top creativity

```html
<!DOCTYPE html>
<html lang="en">
<head>
<meta charset="utf-8">
<title>Project Halcyon – Slide Template</title>
<link rel="stylesheet" href="https://fonts.googleapis.com/css2?family=Nunito+Sans:wght@300;400;700;800&display=swap">
<style>
  :root {
    --blue: #0049b8;
    --navy: #053a8f;
    --board: #e1e1e1;
    --white: #ffffff;
    --ink: #4a4a4a;
    --muted: #b9c3d3;
    --rule: #6f93d6;
    --space-dark: #0a0a0a;
  }
  * { margin: 0; padding: 0; box-sizing: border-box; }
  html, body { width: 803px; height: 1200px; overflow: hidden; }
  body {
    background: var(--board);
    font-family: "Nunito Sans", Arial, sans-serif;
    position: relative;
  }
  .slide {
    position: absolute;
    width: 342px;
    height: 192px;
    overflow: hidden;
    background: var(--white);
    box-shadow: 0 6px 8px rgba(0,0,0,0.18);
  }
  .slide > svg { position: absolute; inset: 0; width: 100%; height: 100%; }
  .slide--blue { background: var(--blue); }
  .slide--navy {
    background: radial-gradient(ellipse 110px 80px at 50% 100%, rgba(90,80,190,0.55), rgba(5,58,143,0) 100%), var(--navy);
  }

  .wordmark {
    position: absolute;
    left: 0; right: 0; top: 72px;
    text-align: center;
    color: var(--white);
    font-weight: 700;
    font-size: 30px;
    letter-spacing: 2px;
    line-height: 1;
  }
  .wordmark small { display: block; font-size: 11px; letter-spacing: 5px; margin-bottom: 3px; }

  .footer-mark {
    position: absolute;
    font-size: 4.5px;
    font-weight: 700;
    color: var(--blue);
    letter-spacing: 0.3px;
  }
  .footer-mark--light { color: var(--white); }
  .page-no {
    position: absolute;
    width: 7px; height: 7px;
    border-radius: 50%;
    background: var(--blue);
    color: var(--white);
    font-size: 3.5px;
    font-weight: 700;
    line-height: 7px;
    text-align: center;
  }
  .page-no--light { background: var(--white); color: var(--blue); }

  .title {
    position: absolute;
    color: var(--blue);
    font-weight: 800;
    line-height: 1.15;
  }
  .title--light { color: var(--white); }

  .agenda { position: absolute; left: 132px; top: 38px; list-style: none; }
  .agenda li {
    height: 25.7px;
    font-size: 8.2px;
    font-weight: 700;
    color: var(--blue);
    white-space: nowrap;
  }
  .agenda span { font-size: 4.2px; font-weight: 400; color: var(--muted); margin-left: 6px; letter-spacing: 0.1px; }

  .body-copy {
    position: absolute;
    font-size: 6.1px;
    line-height: 7.7px;
    color: var(--ink);
    font-weight: 400;
  }
  .body-copy p + p { margin-top: 7.7px; }

  .pull-quote {
    position: absolute;
    right: 16px; top: 28px;
    width: 125px;
    text-align: right;
    color: var(--white);
    font-weight: 300;
    font-size: 12.4px;
    line-height: 15.4px;
  }
</style>
</head>
<body>

<!-- Cover -->
<section class="slide slide--blue" style="left:44px;top:65px">
  <div class="wordmark"><small>PROJECT</small>HALCYON</div>
</section>

<!-- Cover, alternate -->
<section class="slide slide--navy" style="left:417px;top:65px" role="img" aria-label="Cover with faint iridescent planet rising from the bottom edge">
  <div class="wordmark"><small>PROJECT</small>HALCYON</div>
</section>

<!-- Title slide -->
<section class="slide" style="left:44px;top:275px">
  <svg viewBox="0 0 342 192">
    <line x1="73" y1="0" x2="73" y2="93" stroke="var(--blue)" stroke-width="0.8"/>
    <rect x="69.5" y="92" width="7" height="31" rx="3.5" fill="var(--blue)"/>
    <line x1="30" y1="185" x2="326" y2="185" stroke="var(--rule)" stroke-width="0.5"/>
  </svg>
  <h1 class="title" style="left:84px;top:84px;font-size:20px">Your Main Title goes<br>here</h1>
  <div class="footer-mark" style="left:5px;top:182px">HALCYON</div>
  <div class="page-no" style="left:330px;top:181px">4</div>
</section>

<!-- Title slide with arc -->
<section class="slide" style="left:412px;top:279px">
  <svg viewBox="0 0 342 192">
    <path fill="var(--blue)" fill-rule="evenodd" d="M227 24a158 158 0 1 0 0.01 0Z M227 50a132 132 0 1 1 -0.01 0Z"/>
    <line x1="30" y1="185" x2="326" y2="185" stroke="var(--rule)" stroke-width="0.5"/>
  </svg>
  <h1 class="title" style="left:124px;top:140px;font-size:20px">Main Title here</h1>
  <div class="footer-mark" style="left:5px;top:182px">HALCYON</div>
  <div class="page-no" style="left:330px;top:181px">5</div>
</section>

<!-- Contents -->
<section class="slide" style="left:44px;top:493px">
  <svg viewBox="0 0 342 192">
    <rect width="95" height="192" fill="var(--blue)"/>
    <line x1="114" y1="7" x2="114" y2="185" stroke="var(--muted)" stroke-width="0.6"/>
    <g fill="var(--blue)">
      <circle cx="114" cy="44" r="4"/><circle cx="114" cy="69.7" r="4"/><circle cx="114" cy="95.4" r="4"/>
      <circle cx="114" cy="121.1" r="4"/><circle cx="114" cy="146.8" r="4"/>
    </g>
  </svg>
  <h2 class="title title--light" style="left:21px;top:161px;font-size:12px;font-weight:700">Content</h2>
  <ul class="agenda">
    <li>Introduction<span>YOUR INTRODUCTION TITLE</span></li>
    <li>About our team<span>ABOUT OUR TEAM TITLE</span></li>
    <li>Company history<span>COMPANY HISTORY TITLE</span></li>
    <li>Who we are<span>WHO WE ARE TITLE</span></li>
    <li>Our priceing<span>OUR PRICEING TITLE</span></li>
  </ul>
  <div class="footer-mark" style="left:316px;top:182px">HALCYON</div>
</section>

<!-- Section divider -->
<section class="slide slide--blue" style="left:412px;top:493px">
  <svg viewBox="0 0 342 192">
    <line x1="0" y1="142" x2="23" y2="142" stroke="var(--white)" stroke-width="0.6"/>
    <line x1="30" y1="185" x2="326" y2="185" stroke="var(--rule)" stroke-width="0.5"/>
  </svg>
  <h2 class="title title--light" style="left:30px;top:132px;font-size:16px">Section title</h2>
  <div class="footer-mark footer-mark--light" style="left:5px;top:182px">HALCYON</div>
  <div class="page-no page-no--light" style="left:330px;top:181px">7</div>
</section>

<!-- Divider with ring -->
<section class="slide slide--blue" style="left:44px;top:711px">
  <svg viewBox="0 0 342 192">
    <circle cx="351" cy="142" r="151" fill="var(--white)"/>
    <circle cx="351" cy="142" r="123" fill="var(--blue)"/>
    <line x1="0" y1="142" x2="23" y2="142" stroke="var(--white)" stroke-width="0.6"/>
    <line x1="30" y1="185" x2="326" y2="185" stroke="var(--rule)" stroke-width="0.5"/>
  </svg>
  <div class="footer-mark footer-mark--light" style="left:5px;top:182px">HALCYON</div>
  <div class="page-no page-no--light" style="left:330px;top:181px">8</div>
</section>

<!-- Text slide -->
<section class="slide" style="left:412px;top:711px">
  <svg viewBox="0 0 342 192">
    <circle cx="12" cy="0" r="13" fill="none" stroke="var(--blue)" stroke-width="2"/>
    <line x1="30" y1="185" x2="326" y2="185" stroke="var(--rule)" stroke-width="0.5"/>
  </svg>
  <h2 class="title" style="left:26px;top:12px;font-size:14px">Main Title here</h2>
  <div class="body-copy" style="left:28px;top:37px;width:300px">
    <p>Lorem ipsum dolor sit amet, consectetuer adipiscing elit. Maecenas porttitor congue massa. Fusce posuere, magna sed pulvinar ultricies, purus lectus malesuada libero, sit amet commodo magna eros quis urna.</p>
    <p>Nunc viverra imperdiet enim. Fusce est. Vivamus a tellus.</p>
    <p>Pellentesque habitant morbi tristique senectus et netus et malesuada fames ac turpis egestas. Proin pharetra nonummy pede. Mauris et orci.<br>Nunc viverra imperdiet enim. Fusce est. Vivamus a tellus.</p>
    <p>Pellentesque habitant morbi tristique senectus et netus et malesuada fames ac turpis egestas. Proin pharetra nonummy pede. Mauris et orci.</p>
  </div>
  <div class="footer-mark" style="left:5px;top:182px">HALCYON</div>
  <div class="page-no" style="left:330px;top:181px">9</div>
</section>

<!-- Text with image -->
<section class="slide" style="left:44px;top:929px">
  <svg viewBox="0 0 342 192">
    <circle cx="283" cy="89" r="94" fill="var(--blue)"/>
    <defs>
      <radialGradient id="bubble" cx="0.35" cy="0.8" r="0.7">
        <stop offset="0" stop-color="#8a3a7a"/>
        <stop offset="0.45" stop-color="#2a3a6a"/>
        <stop offset="1" stop-color="var(--space-dark)"/>
      </radialGradient>
    </defs>
    <circle cx="279" cy="91" r="92" fill="url(#bubble)" role="img" aria-label="Photo of an iridescent soap bubble against a black background"/>
    <circle cx="12" cy="0" r="13" fill="none" stroke="var(--blue)" stroke-width="2"/>
    <line x1="30" y1="185" x2="326" y2="185" stroke="var(--rule)" stroke-width="0.5"/>
  </svg>
  <h2 class="title" style="left:26px;top:12px;font-size:14px">Main Title here</h2>
  <div class="body-copy" style="left:28px;top:37px;width:154px">
    <p>Lorem ipsum dolor sit amet, consectetuer adipiscing elit. Maecenas porttitor congue massa. Fusce posuere, magna sed pulvinar ultricies, purus lectus malesuada libero, sit amet commodo magna eros quis urna.</p>
    <p>Nunc viverra imperdiet enim. Fusce est. Vivamus a tellus.</p>
    <p>Pellentesque habitant morbi tristique senectus et netus et malesuada fames ac turpis egestas. Proin pharetra nonummy pede. Mauris et orci. Nunc viverra imperdiet enim. Fusce est. Vivamus a tellus.</p>
    <p>Pellentesque habitant morbi tristique senectus et netus et malesuada fames ac turpis egestas. Proin pharetra nonummy pede. Mauris et orci.</p>
  </div>
  <div class="footer-mark" style="left:5px;top:182px">HALCYON</div>
  <div class="page-no" style="left:330px;top:181px">10</div>
</section>

<!-- Text with quote -->
<section class="slide" style="left:412px;top:929px">
  <svg viewBox="0 0 342 192">
    <circle cx="287" cy="82" r="100" fill="var(--blue)"/>
    <circle cx="12" cy="0" r="13" fill="none" stroke="var(--blue)" stroke-width="2"/>
    <line x1="30" y1="185" x2="326" y2="185" stroke="var(--rule)" stroke-width="0.5"/>
  </svg>
  <h2 class="title" style="left:26px;top:12px;font-size:14px">Main Title here</h2>
  <div class="body-copy" style="left:28px;top:37px;width:154px">
    <p>Lorem ipsum dolor sit amet, consectetuer adipiscing elit. Maecenas porttitor congue massa. Fusce posuere, magna sed pulvinar ultricies, purus lectus malesuada libero, sit amet commodo magna eros quis urna.</p>
    <p>Nunc viverra imperdiet enim. Fusce est. Vivamus a tellus.</p>
    <p>Pellentesque habitant morbi tristique senectus et netus et malesuada fames ac turpis egestas. Proin pharetra nonummy pede. Mauris et orci. Nunc viverra imperdiet enim. Fusce est. Vivamus a tellus.</p>
    <p>Pellentesque habitant morbi tristique senectus et netus et malesuada fames ac turpis egestas. Proin pharetra nonummy pede. Mauris et orci.</p>
  </div>
  <p class="pull-quote">Lorem ipsum dolor sit amet, consectetuer adipiscing elit. Maecenas porttitor congue massa. Fusce posuere</p>
  <div class="footer-mark" style="left:5px;top:182px">HALCYON</div>
  <div class="page-no" style="left:330px;top:181px">11</div>
</section>

</body>
</html>
```